New Stationary for our business

We are a gift business and would like to create a new corporate image with new stationary and design.

We would like a Classic Corporate look with a touch of Flair.

We would need:
Envelopes
Letter Head
Business Cards
With Comp Slips
Note Pads
Etc...

Our details are:

Basket Haven Pty Ltd
518 Pelling Street, Carrow Vale, Victoria, 3071
1800 742 918
www.baskethaven.com.au
sales@baskethaven.com.au

ABN: 62 804 319 775

Target Market(s)

Corporate Look

Industry/Entity Type

Marketing

Contact Information for Business Card

Basket Haven Pty Ltd
1800 742 918
518 Pelling Street
Carrow Vale 3071
Victoria Australia

Darren Pelloni - Managing Director
darren.pelloni@baskethaven.com.au
0417 586 902

Logo Text

Basket Haven - The Present Experts

Colors

Designer to choose colors to be used in the design.

Requirements
Must have
• Look and Feel upmarket and exclusive

```html
<!DOCTYPE html>
<html lang="en">
<head>
<meta charset="utf-8">
<title>Basket Haven – Stationery Suite</title>
<link rel="stylesheet" href="https://fonts.googleapis.com/css2?family=Oswald:wght@300;400&family=Open+Sans:wght@400;600;700&display=swap">
<style>
  :root {
    --bg: #d6d7d9;
    --gold: #b09c72;
    --gold-dark: #9c8960;
    --charcoal: #414042;
    --paper: #ffffff;
    --ink: #3a3a3c;
    --muted: #6d6d70;
    --brand-font: "Oswald", sans-serif;
    --body-font: "Open Sans", sans-serif;
  }
  * { box-sizing: border-box; margin: 0; padding: 0; }
  html, body { width: 1200px; height: 1200px; overflow: hidden; }
  body { background: var(--bg); font-family: var(--body-font); color: var(--ink); position: relative; }

  .piece { position: absolute; background: var(--paper); }

  /* Brand lockup: name + one plain circle */
  .brand { position: absolute; display: flex; align-items: center; gap: .35em; font-family: var(--brand-font); font-weight: 400; color: var(--charcoal); text-transform: uppercase; white-space: nowrap; letter-spacing: .01em; line-height: 1; }
  .brand-dot { width: .7em; height: .7em; border-radius: 50%; background: var(--gold); flex: none; }
  .brand.centered { transform: translateX(-50%); }

  /* Hero */
  .hero-brand { left: 600px; top: 190px; font-size: 54px; }
  .hero-tagline { position: absolute; left: 600px; top: 244px; transform: translateX(-50%); display: flex; align-items: center; gap: 10px; font-family: var(--brand-font); font-weight: 300; font-size: 18px; line-height: 1; color: var(--gold); white-space: nowrap; text-transform: uppercase; }
  .hero-tagline::before, .hero-tagline::after { content: ""; width: 52px; height: 1px; background: var(--gold); }
  .hero-abn { position: absolute; left: 600px; top: 266px; transform: translateX(-50%); font-family: var(--brand-font); font-size: 9px; line-height: 1; color: var(--charcoal); white-space: nowrap; }

  /* Presentation folder */
  .folder-flap-side { position: absolute; left: 134px; top: 395px; width: 44px; height: 340px; background: var(--charcoal); clip-path: polygon(100% 0, 100% 100%, 0 88%, 0 6%); }
  .folder-cover { position: absolute; left: 178px; top: 384px; width: 223px; height: 308px; background: var(--gold); }
  .folder-pocket { position: absolute; left: 178px; top: 692px; width: 223px; height: 52px; background: var(--charcoal); clip-path: polygon(0 0, 100% 0, 84% 100%, 0 100%); }
  .folder-inside { left: 401px; top: 384px; width: 223px; height: 308px; }
  .folder-footer { position: absolute; left: 48px; bottom: 18px; display: flex; gap: 12px; font-size: 3.2px; color: var(--charcoal); }
  .folder-footer span, .folder-web { display: flex; align-items: center; gap: 2px; }
  .icon-dot { width: 4px; height: 4px; border-radius: 50%; background: var(--charcoal); flex: none; }
  .folder-web { position: absolute; left: 100px; bottom: 14px; font-size: 3.2px; color: var(--charcoal); }

  /* Letterhead */
  .letterhead { left: 661px; top: 386px; width: 217px; height: 308px; }
  .lh-contact { position: absolute; right: 26px; top: 30px; text-align: right; font-size: 3.3px; line-height: 4.4px; color: var(--muted); }
  .lh-salutation { position: absolute; left: 32px; top: 77px; font-size: 3.6px; line-height: 4.4px; }
  .lh-salutation strong, .lh-date, .lh-sign strong { font-weight: 700; color: var(--ink); }
  .lh-date { position: absolute; right: 31px; top: 77px; font-size: 3.6px; }
  .lh-body { position: absolute; left: 32px; top: 102px; width: 154px; font-size: 3.5px; line-height: 4.4px; color: var(--muted); text-align: justify; }
  .lh-body p + p { margin-top: 7px; }
  .lh-sign { position: absolute; right: 31px; top: 248px; font-size: 3.6px; line-height: 4.6px; text-align: right; }
  .lh-sign-line { display: block; width: 32px; height: 1px; background: var(--muted); margin: 8px 0 0 auto; }
  .lh-band { position: absolute; left: 0; right: 0; bottom: 10px; height: 4px; background: var(--gold); }
  .lh-band-dot { position: absolute; left: 50%; bottom: 6px; width: 12px; height: 12px; margin-left: -6px; border-radius: 50%; background: var(--paper); border: 2px solid var(--gold); }

  /* Business cards */
  .card { width: 173px; height: 100px; box-shadow: 0 1px 2px rgba(0,0,0,.06); }
  .card-front { left: 864px; top: 450px; background: var(--gold); overflow: hidden; }
  .card-front svg { position: absolute; inset: 0; }
  .card-front .brand { color: var(--paper); font-size: 10px; left: 10px; top: 45px; }
  .card-front .brand-dot { background: var(--paper); }
  .card-name { position: absolute; left: 96px; top: 33px; font-family: var(--brand-font); font-size: 7px; line-height: 1; color: var(--charcoal); }
  .card-list { position: absolute; left: 96px; top: 48px; list-style: none; font-size: 3.3px; line-height: 7px; color: var(--muted); }
  .card-list li { display: flex; align-items: flex-start; gap: 4px; }
  .card-list .icon-dot { background: var(--gold); margin-top: 1.5px; }
  .card-back { left: 864px; top: 562px; }
  .card-back .brand { left: 86px; top: 44px; font-size: 11px; }

  /* Large envelope */
  .envelope-large { left: 175px; top: 776px; width: 214px; height: 304px; }
  .flap { position: absolute; left: 0; right: 0; top: 0; background: var(--charcoal); }
  .envelope-large .flap { height: 36px; clip-path: polygon(0 0, 100% 0, 100% 70%, 97% 100%, 3% 100%, 0 70%); }
  .env-contact { position: absolute; left: 18px; bottom: 20px; font-size: 4px; line-height: 6.5px; color: var(--ink); }

  /* Note pad */
  .notepad { left: 402px; top: 776px; width: 213px; height: 304px; }
  .notepad .brand { left: 45px; top: 38px; font-size: 8px; }
  .notepad-address { position: absolute; left: 45px; top: 56px; transform: translateX(-50%); text-align: center; font-size: 3.6px; line-height: 4.6px; color: var(--ink); white-space: nowrap; }

  /* Compliments slip */
  .comp-slip { left: 496px; top: 994px; width: 269px; height: 124px; box-shadow: 0 1px 2px rgba(0,0,0,.06); }
  .comp-slip .brand { left: 44px; top: 28px; font-size: 8px; }
  .comp-contact { position: absolute; left: 22px; top: 66px; font-size: 5px; line-height: 5.8px; color: var(--ink); }
  .comp-band { position: absolute; left: 0; bottom: 8px; width: 131px; height: 16px; background: var(--gold); clip-path: polygon(0 0, 88% 0, 100% 100%, 0 100%); color: var(--paper); font-family: var(--body-font); font-weight: 700; font-size: 6px; letter-spacing: .08em; text-transform: uppercase; display: flex; align-items: center; padding-left: 22px; }

  /* DL envelopes */
  .dl-back { left: 704px; top: 757px; width: 274px; height: 137px; }
  .dl-back .flap { height: 41px; clip-path: polygon(0 0, 100% 0, 100% 55%, 96% 100%, 4% 100%, 0 55%); }
  .dl-front { left: 798px; top: 872px; width: 275px; height: 138px; box-shadow: 0 1px 3px rgba(0,0,0,.08); }
  .dl-window { position: absolute; left: 20px; top: 52px; width: 93px; height: 48px; border-radius: 9px; background: linear-gradient(135deg, var(--gold) 0%, #c8b78f 55%, var(--gold-dark) 100%); }
  .dl-front .brand { right: 18px; top: 38px; font-size: 8px; }
  .dl-contact { position: absolute; right: 18px; top: 95px; text-align: right; font-size: 5px; line-height: 5.8px; color: var(--ink); }
</style>
</head>
<body>

  <!-- Primary lockup -->
  <div class="brand centered hero-brand"><span class="brand-dot"></span>Basket Haven</div>
  <div class="hero-tagline">The Present Experts</div>
  <div class="hero-abn">ABN: 62 804 319 775</div>

  <!-- Presentation folder -->
  <div class="folder-flap-side"></div>
  <div class="folder-cover">
    <div class="folder-footer">
      <span><i class="icon-dot"></i>1800 742 918</span>
      <span><i class="icon-dot"></i>sales@baskethaven.com.au</span>
      <span><i class="icon-dot"></i>518 Pelling Street, Carrow Vale,<br>Victoria, 3071</span>
    </div>
  </div>
  <div class="folder-pocket"></div>
  <div class="piece folder-inside">
    <div class="brand centered" style="left:112px; top:160px; font-size:15px;"><span class="brand-dot"></span>Basket Haven</div>
    <div class="folder-web"><i class="icon-dot"></i>www.baskethaven.com.au</div>
  </div>

  <!-- Letterhead -->
  <div class="piece letterhead">
    <div class="brand" style="left:30px; top:46px; font-size:7px;"><span class="brand-dot"></span>Basket Haven</div>
    <div class="lh-contact">
      1800 742 918<br>
      sales@baskethaven.com.au<br>
      518 Pelling Street, Carrow Vale,<br>
      Victoria, 3071<br>
      www.baskethaven.com.au
    </div>
    <div class="lh-salutation"><strong>Dear, Mr_________</strong><br>Designation<br><strong>COMPANY NAME</strong></div>
    <div class="lh-date">DATE:1/3/2018</div>
    <div class="lh-body">
      <p>Thank you for choosing us for your corporate gifting this season. Every hamper we send is packed by hand with local produce, fine wines and thoughtful treats, then wrapped and delivered on the date you request to each person on your list.</p>
      <p>Our team can add your company card, a printed message or a branded ribbon to any order. Larger orders may be sent in stages, and we are glad to suggest gifts that suit your budget and the people you wish to thank.</p>
      <p>Please review the enclosed price list and order form at your leisure. Prices include wrapping and a gift card, while delivery is charged by region. Orders placed before the first of the month receive priority dispatch and a small bonus treat.</p>
      <p>Should you have any questions about your order, our staff are happy to help by phone or email during business hours. We look forward to working with you again and to making your next celebration truly memorable for all.</p>
    </div>
    <div class="lh-sign"><strong>YOUR NAME</strong><br>Designation<span class="lh-sign-line"></span></div>
    <div class="lh-band"></div>
    <div class="lh-band-dot"></div>
  </div>

  <!-- Business card, front -->
  <div class="piece card card-front">
    <svg width="173" height="100" viewBox="0 0 173 100" aria-hidden="true">
      <path d="M173 0 H118 C92 14 84 34 84 50 C84 66 92 86 118 100 H173 Z" fill="#ffffff"/>
    </svg>
    <div class="brand"><span class="brand-dot"></span>Basket Haven</div>
    <div class="card-name">Basket Haven Pty Ltd</div>
    <ul class="card-list">
      <li><i class="icon-dot"></i>1800 742 918</li>
      <li><i class="icon-dot"></i>sales@baskethaven.com.au</li>
      <li><i class="icon-dot"></i>www.baskethaven.com.au</li>
      <li><i class="icon-dot"></i><span>518 Pelling Street, Carrow Vale,<br>Victoria, 3071</span></li>
    </ul>
  </div>

  <!-- Business card, back -->
  <div class="piece card card-back">
    <div class="brand centered"><span class="brand-dot"></span>Basket Haven</div>
  </div>

  <!-- Large envelope -->
  <div class="piece envelope-large">
    <div class="flap"></div>
    <div class="env-contact">1800 742 918<br>sales@baskethaven.com.au<br>www.baskethaven.com.au</div>
  </div>

  <!-- Note pad -->
  <div class="piece notepad">
    <div class="brand centered"><span class="brand-dot"></span>Basket Haven</div>
    <div class="notepad-address">518 Pelling Street, Carrow Vale,<br>Victoria, 3071</div>
  </div>

  <!-- Compliments slip -->
  <div class="piece comp-slip">
    <div class="brand centered"><span class="brand-dot"></span>Basket Haven</div>
    <div class="comp-contact">1800 742 918<br>sales@baskethaven.com.au<br>518 Pelling Street, Carrow Vale,<br>Victoria, 3071<br>www.baskethaven.com.au</div>
    <div class="comp-band">With Compliments</div>
  </div>

  <!-- DL envelope, back -->
  <div class="piece dl-back">
    <div class="flap"></div>
  </div>

  <!-- DL envelope, front -->
  <div class="piece dl-front">
    <div class="dl-window"></div>
    <div class="brand"><span class="brand-dot"></span>Basket Haven</div>
    <div class="dl-contact">1800 742 918<br>sales@baskethaven.com.au<br>518 Pelling Street, Carrow Vale,<br>Victoria, 3071<br>www.baskethaven.com.au</div>
  </div>

</body>
</html>
```